Federal Research Council Vast Records PI Summit 2016

We need a poster for a FRC-sponsored (Federal Research Council) project presented by Halvorsen University and the University of Westbrook Plains on April 20-21, 2016.

This is what the project will be about: (of course this is something that the audience/participants of this project will understand) The growth in scale, diversity, and complexity of data has increased the demand for understanding large amounts of heterogeneous data. This presents new challenges to the way data and information are used and managed. The goal of the two-day workshop is to bring together PIs and co-PIs currently funded by the Vast Records program at FRC along with selected industry and government invitees to discuss current research, identify current challenges, and discuss promising future directions.

Possible key words to incorporate: data analytics, security, machine learning, social, environment, health, medicine, energy, data visualization, optimization, scalable algorithms, data mining, massive data, privacy, data ethics

The key words we included were for two purposes:

- for data-related graphics ideas (i.e. images of data visualization
graphs or machine learning, etc.)
- or to use some or all of the actual words throughout the poster

- Poster size - Height = 34.5 inches
Width = 27.5 inches

- No contact info needed.

- Date - April 20th-21st (exact time not needed)

- Location - Arlington, VA

- Text - Federal Research Council
Vast Records PI Summit - 2016
April 20th-21st
Arlington, VA

***Federal Research Council and Vast Records PI Summit 2016 need to be
significantly bigger than the other text.

That is the only required text.

We'd like to see the colors that are shades of blue, yellow/gold and (possibly) red.

We've attached the two university logos to incorporate into the design.
- Images/photos – We don’t have photos but will be happy to see data
science-related images. We're open to photos of groups of people showing
diversity; please don't use an image of just one person. If we need to pay
for it, please provide the link for purchase, so we can check it out. Thank
you.

Thank you for submitting your designs. We won't be able to review them until Monday March 28th and will adjust the deadline as needed. Added Saturday, March 26, 2016

Target Market(s)

Researchers and government employees in various disciplines: data science, engineering, mathematics, health, climate, sociology

Industry/Entity Type

University

Font styles to use
Serif

Colors
f04a50
3276b5
fece3e

Requirements
Must have
• FRC VRPI - 2016 Meeting
• Arlington, VA
• April 20th-21st
• University logos

```html
<!DOCTYPE html>
<html lang="en">
<head>
<meta charset="utf-8">
<title>Federal Research Council – Vast Records PI Summit 2016</title>
<link rel="stylesheet" href="https://fonts.googleapis.com/css2?family=Old+Standard+TT&family=Cutive&display=swap">
<style>
  :root {
    --paper: #ffffff;
    --ink: #000000;
    --red: #f04a50;
    --blue: #3276b5;
    --gold: #fece3e;
  }
  html, body { margin: 0; padding: 0; overflow: hidden; background: var(--paper); }
  .poster { display: block; width: 927px; height: 1200px; }
  .headline { font-family: "Old Standard TT", serif; font-size: 42px; fill: var(--ink); }
  .event-info { font-family: "Old Standard TT", serif; font-size: 30px; fill: var(--ink); }
  .cloud-outline, .bubble { fill: var(--paper); stroke: var(--ink); stroke-width: 5; }
  .word { font-family: "Cutive", serif; }
  .word--red { fill: var(--red); }
  .word--blue { fill: var(--blue); }
  .word--gold { fill: var(--gold); }
  .fineprint { font-family: "Old Standard TT", serif; font-size: 3px; fill: var(--ink); }
  .partner-mark { fill: none; stroke: var(--ink); stroke-width: 1.5; }
  .partner-name { font-family: "Old Standard TT", serif; font-size: 8px; fill: var(--ink); text-anchor: middle; }
</style>
</head>
<body>
<svg class="poster" viewBox="0 0 600 776.7" xmlns="http://www.w3.org/2000/svg">
  <rect width="600" height="776.7" fill="var(--paper)"/>

  <g class="title">
    <text class="headline" x="42" y="82" textLength="538" lengthAdjust="spacingAndGlyphs">Federal Research Council</text>
    <text class="headline" x="60" y="144" textLength="505" lengthAdjust="spacingAndGlyphs">Vast Records PI Summit - 2016</text>
  </g>

  <g class="thought-bubble">
    <ellipse class="bubble" cx="150" cy="512" rx="28" ry="17"/>
    <ellipse class="bubble" cx="128" cy="563" rx="33" ry="20"/>
    <ellipse class="bubble" cx="115" cy="614" rx="37" ry="21"/>
    <path class="cloud-outline" d="M150 235 C120 175,200 150,240 170 C290 140,380 145,420 175 C470 160,530 200,520 260 C575 290,575 370,545 410 C575 450,550 520,480 515 C440 545,360 540,320 520 C270 545,200 535,175 500 C110 510,65 470,85 420 C35 390,40 300,100 290 C95 260,115 240,150 235 Z"/>
  </g>

  <g class="word-cloud">
    <text class="word word--blue" x="172" y="188" font-size="17" textLength="50" lengthAdjust="spacingAndGlyphs">data</text>
    <text class="word word--blue" x="172" y="215" font-size="18" textLength="148" lengthAdjust="spacingAndGlyphs">visualization</text>
    <text class="word word--red" transform="translate(166 316) rotate(-90)" font-size="34" textLength="140" lengthAdjust="spacingAndGlyphs">privacy</text>
    <text class="word word--red" x="178" y="258" font-size="42" textLength="202" lengthAdjust="spacingAndGlyphs">security</text>
    <text class="word word--gold" transform="translate(385 180) rotate(90)" font-size="17" textLength="120" lengthAdjust="spacingAndGlyphs">optimization</text>
    <text class="word word--gold" transform="translate(413 188) rotate(90)" font-size="10" textLength="105" lengthAdjust="spacingAndGlyphs">machine learning</text>
    <text class="word word--gold" x="178" y="302" font-size="30" textLength="196" lengthAdjust="spacingAndGlyphs">data ethics</text>
    <text class="word word--red" x="440" y="307" font-size="26" textLength="103" lengthAdjust="spacingAndGlyphs">health</text>
    <text class="word word--blue" x="60" y="352" font-size="48" textLength="497" lengthAdjust="spacingAndGlyphs">heterogeneous data</text>
    <text class="word word--gold" x="85" y="384" font-size="31" textLength="128" lengthAdjust="spacingAndGlyphs">energy</text>
    <text class="word word--gold" transform="translate(282 521) rotate(-90)" font-size="22" textLength="157" lengthAdjust="spacingAndGlyphs">data mining</text>
    <text class="fineprint" x="289" y="358">FRC VRPI - 2016 Meeting</text>
    <text class="fineprint" x="289" y="362">Arlington VA April 20-21</text>
    <text class="word word--red" x="292" y="378" font-size="24" textLength="268" lengthAdjust="spacingAndGlyphs">scalable algorithms</text>
    <text class="word word--red" x="90" y="412" font-size="33" textLength="172" lengthAdjust="spacingAndGlyphs">medicine</text>
    <text class="word word--blue" x="310" y="400" font-size="22" textLength="80" lengthAdjust="spacingAndGlyphs">social</text>
    <text class="word word--blue" x="155" y="430" font-size="20" textLength="58" lengthAdjust="spacingAndGlyphs">data</text>
    <text class="word word--gold" x="336" y="428" font-size="28" textLength="196" lengthAdjust="spacingAndGlyphs">environment</text>
    <text class="word word--blue" x="150" y="460" font-size="22" textLength="108" lengthAdjust="spacingAndGlyphs">analytics</text>
    <text class="word word--blue" x="287" y="466" font-size="34" textLength="234" lengthAdjust="spacingAndGlyphs">massive data</text>
  </g>

  <g class="event">
    <text class="event-info" x="222" y="646" textLength="156" lengthAdjust="spacingAndGlyphs">April 20-21</text>
    <text class="event-info" x="207" y="690" textLength="165" lengthAdjust="spacingAndGlyphs">Arlington VA</text>
  </g>

  <g class="partners">
    <g class="partner partner--westbrook">
      <circle class="partner-mark" cx="520" cy="548" r="22"/>
      <text class="partner-name" x="520" y="586">University of</text>
      <text class="partner-name" x="520" y="596">Westbrook Plains</text>
    </g>
    <g class="partner partner--halvorsen">
      <circle class="partner-mark" cx="520" cy="657" r="26"/>
      <text class="partner-name" x="520" y="700">Halvorsen University</text>
    </g>
  </g>
</svg>
</body>
</html>
```